Health and wellnes company needs business cards

We are a Health and wellness business just relocated to Spain. Here nobody knows our business so we would like to put some of our services on the card. Clean design with logo.

Contact Information for Business Card

Brightmeadow
Clara & Tobias Wennberg
Calle de los Almendros 17
Villaluz de la Costa
Mobile: 0046 731 402768
info@brightmeadow-example.se

Font styles to use
Serif

Colors
85cae6
85acd3
b768aa

Requirements
Must have
• these Services somewhere on the card
• - Private or group yoga
• - Reconnective healing
• - Kitesurfing lessons
• - Massage
• LOgo somewhere
Nice to have
• Colours that go with the logo please

```html
<!DOCTYPE html>
<html lang="en">
<head>
<meta charset="utf-8">
<title>Brightmeadow business card</title>
<link href="https://fonts.googleapis.com/css2?family=Roboto:wght@400;500;700&display=swap" rel="stylesheet">
<style>
  :root {
    --navy: #1b365f;
    --teal: #6ec6c8;
    --paper: #f8f9fb;
    --ink: #4a4a4a;
    --backdrop: #b9b9b9;
  }
  * { margin: 0; padding: 0; box-sizing: border-box; }
  html, body {
    width: 1172px; height: 1200px; overflow: hidden;
    background: var(--backdrop);
    font-family: "Roboto", Arial, sans-serif;
  }
  .card {
    position: absolute; left: 214px; width: 744px;
  }
  .card-front { top: 122px; height: 425px; background: var(--navy); }
  .card-back { top: 645px; height: 430px; background: var(--paper); }

  .brand-mark {
    position: absolute; border-radius: 50%;
    background: var(--teal);
  }
  .card-front .brand-mark { width: 148px; height: 148px; left: 298px; top: 103px; }
  .card-back .brand-mark { width: 108px; height: 108px; left: 542px; top: 34px; }

  .brand-name {
    position: absolute; left: 0; text-align: center;
    font-weight: 500; letter-spacing: 1px; text-transform: uppercase; white-space: nowrap;
  }
  .card-front .brand-name {
    width: 744px; top: 265px; font-size: 42px; line-height: 50px; color: #f2f2f4;
  }
  .card-back .brand-name {
    width: 260px; left: 466px; top: 150px; font-size: 27px; line-height: 34px; color: var(--navy);
  }

  .website {
    position: absolute; top: 361px; width: 744px; text-align: center;
    font-size: 22px; letter-spacing: 2.5px; color: #f2f2f4;
  }
  .website .accent { color: var(--teal); }

  .name-marker {
    position: absolute; left: 0; top: 153px; width: 10px; height: 51px; background: var(--navy);
  }
  .person-name {
    position: absolute; left: 26px; top: 148px;
    font-size: 29px; font-weight: 700; color: var(--navy); white-space: nowrap;
  }
  .person-role {
    position: absolute; left: 26px; top: 185px; font-size: 21px; color: var(--teal);
  }
  .address {
    position: absolute; left: 26px; top: 239px;
    font-size: 21px; line-height: 29px; color: var(--ink);
  }
  .contact-list { position: absolute; left: 26px; top: 333px; list-style: none; }
  .contact-list li {
    display: flex; align-items: center; gap: 10px;
    font-size: 21px; line-height: 28px; color: var(--ink);
  }
  .contact-list svg { width: 17px; height: 17px; flex: none; }

  .services-title {
    position: absolute; left: 482px; top: 240px;
    font-size: 23px; font-weight: 700; color: var(--navy);
  }
  .services-list { position: absolute; left: 482px; top: 277px; list-style: none; }
  .services-list li {
    position: relative; padding-left: 24px;
    font-size: 21px; line-height: 28px; color: var(--ink); white-space: nowrap;
  }
  .services-list li::before {
    content: ""; position: absolute; left: 1px; top: 9px;
    width: 10px; height: 10px; border-radius: 50%; background: var(--navy);
  }

  .footer-band {
    position: absolute; left: 0; bottom: 0; width: 744px; height: 18px;
    background: linear-gradient(to right, var(--navy) 0 482px, var(--teal) 482px 100%);
  }
</style>
</head>
<body>
  <section class="card card-front">
    <div class="brand-mark"></div>
    <div class="brand-name">Brightmeadow</div>
    <div class="website"><span class="accent">www.</span>brightmeadow<span class="accent">.com</span></div>
  </section>

  <section class="card card-back">
    <div class="name-marker"></div>
    <h1 class="person-name">Clara &amp; Tobias Wennberg</h1>
    <p class="person-role">Co-Founder</p>
    <p class="address">Calle de los Almendros 17<br>Villaluz de la Costa</p>
    <ul class="contact-list">
      <li>
        <svg viewBox="0 0 24 24" aria-hidden="true"><path fill="#1b365f" d="M6.6 10.8a15.1 15.1 0 0 0 6.6 6.6l2.2-2.2a1 1 0 0 1 1-.25 11.4 11.4 0 0 0 3.6.57 1 1 0 0 1 1 1V20a1 1 0 0 1-1 1A17 17 0 0 1 3 4a1 1 0 0 1 1-1h3.5a1 1 0 0 1 1 1c0 1.25.2 2.45.57 3.57a1 1 0 0 1-.25 1z"/></svg>
        0046 731 402768
      </li>
      <li>
        <svg viewBox="0 0 24 24" aria-hidden="true"><rect x="2" y="5" width="20" height="14" fill="none" stroke="#1b365f" stroke-width="2"/><path d="M2 5l10 8 10-8" fill="none" stroke="#1b365f" stroke-width="2"/></svg>
        info@brightmeadow-example.se
      </li>
    </ul>

    <div class="brand-mark"></div>
    <div class="brand-name">Brightmeadow</div>

    <h2 class="services-title">Services</h2>
    <ul class="services-list">
      <li>Private or group yoga</li>
      <li>Reconnective healing</li>
      <li>Kitesurfing lessons</li>
      <li>Massage</li>
    </ul>

    <div class="footer-band"></div>
  </section>
</body>
</html>
```